Construction Company Business Card

Business Card Design using new Logo

Contact Information for Business Card

include all company info and website

Requirements
Must have
• Wesley Corman - President
ph. 254-617-0382
Cedar Knoll, TX
wesley@ironmarkframing.com
www.ironmarkframing.com

```html
<!DOCTYPE html>
<html lang="en">
<head>
<meta charset="utf-8">
<title>Ironmark Framing Texas — Business Card</title>
<link href="https://fonts.googleapis.com/css2?family=Montserrat:wght@400;500;600;700&display=swap" rel="stylesheet">
<style>
  :root {
    --stage: #1c1c1c;
    --brand-red: #c8222b;
    --brand-red-deep: #a91b23;
    --paper: #ffffff;
    --ink-grey: #555555;
    --logo-grey: #a9a9a9;
  }
  * { box-sizing: border-box; margin: 0; padding: 0; }
  html, body {
    width: 1200px; height: 900px; overflow: hidden;
    background: var(--stage);
    font-family: "Montserrat", sans-serif;
  }
  .canvas { position: relative; width: 1200px; height: 900px; }

  .card {
    position: absolute;
    width: 560px; height: 320px;
    left: 320px;
    box-shadow: 0 10px 30px rgba(0,0,0,0.5);
  }

  /* Front */
  .card-front { top: 100px; background: var(--brand-red); display: flex; align-items: center; justify-content: center; }
  .front-wordmark {
    color: var(--brand-red-deep);
    font-weight: 600; font-size: 30px; letter-spacing: 3px;
    text-transform: uppercase; text-align: center; line-height: 1.25;
  }

  /* Back */
  .card-back { top: 470px; background: var(--paper); }
  .back-wordmark {
    position: absolute; left: 40px; top: 40px;
    display: flex; align-items: center; gap: 10px;
  }
  .back-wordmark .mark-square { width: 14px; height: 14px; background: var(--brand-red); }
  .back-wordmark .mark-name {
    color: var(--logo-grey); font-weight: 600; font-size: 19px;
    letter-spacing: 2px; text-transform: uppercase; line-height: 1.2;
  }

  .divider {
    position: absolute; left: 40px; right: 40px; top: 200px;
    height: 1.5px; background: var(--brand-red);
  }

  .identity { position: absolute; right: 40px; top: 148px; text-align: right; }
  .identity .person-name {
    color: var(--brand-red); font-weight: 700; font-size: 24px; letter-spacing: 1.5px;
    text-transform: uppercase; line-height: 1;
  }
  .identity .person-title { color: var(--ink-grey); font-size: 15px; margin-top: 6px; }

  .edge-tab {
    position: absolute; right: 0; top: 150px; width: 8px; height: 50px;
    background: var(--brand-red);
  }

  .contact-list {
    position: absolute; left: 40px; top: 214px; list-style: none;
  }
  .contact-list li {
    display: flex; align-items: center; gap: 8px;
    color: var(--ink-grey); font-size: 15px; line-height: 21px;
  }
  .contact-list svg { width: 12px; height: 12px; flex: none; }
</style>
</head>
<body>
<div class="canvas">

  <section class="card card-front">
    <div class="front-wordmark">Ironmark Framing<br>Texas</div>
  </section>

  <section class="card card-back">
    <div class="back-wordmark">
      <span class="mark-square"></span>
      <span class="mark-name">Ironmark Framing<br>Texas</span>
    </div>

    <div class="identity">
      <div class="person-name">Wesley Corman</div>
      <div class="person-title">President</div>
    </div>
    <div class="edge-tab"></div>
    <div class="divider"></div>

    <ul class="contact-list">
      <li>
        <svg viewBox="0 0 12 12" aria-hidden="true"><path d="M3 1 L5 3.5 L4 4.8 Q5 7 7.2 8 L8.5 7 L11 9 L9.8 11 Q5 11 2 7 Q0.5 4 1.5 1.8 Z" fill="#c8222b"/></svg>
        254-617-0382
      </li>
      <li>
        <svg viewBox="0 0 12 12" aria-hidden="true"><rect x="0.8" y="2.5" width="10.4" height="7" fill="none" stroke="#c8222b" stroke-width="1.3"/><path d="M1 3 L6 7 L11 3" fill="none" stroke="#c8222b" stroke-width="1.3"/></svg>
        wesley@ironmarkframing.com
      </li>
      <li>
        <svg viewBox="0 0 12 12" aria-hidden="true"><circle cx="6" cy="6" r="5" fill="none" stroke="#c8222b" stroke-width="1.1"/><ellipse cx="6" cy="6" rx="2.2" ry="5" fill="none" stroke="#c8222b" stroke-width="1"/><path d="M1 6 H11" stroke="#c8222b" stroke-width="1"/></svg>
        www.ironmarkframing.com
      </li>
      <li>
        <svg viewBox="0 0 12 12" aria-hidden="true"><path d="M6 11.5 Q2 7 2 4.5 A4 4 0 0 1 10 4.5 Q10 7 6 11.5 Z" fill="#c8222b"/><circle cx="6" cy="4.5" r="1.5" fill="#fff"/></svg>
        Cedar Knoll, TX
      </li>
    </ul>
  </section>

</div>
</body>
</html>
```